Looking for amazing PowerPoint Design for sustainable, green last mile delivery company

What we need
- PowerPoint master (16:9)
- Min. 20-30 most used template slides
- Templates for tables, processes, gantt chart, etc.
- Would be good to make it look very modern, green/sustainable, human
- Feel free to extend the color range in addition to the 2 colors from our logo

Who we are
- https://www.brookvane-freight.de/index1.php
- Brookvane Freight is a pioneer in urban green logistics and provides zero-emissions last mile delivery services for its logistics and retail clients
- we take on urban parcel delivery for our clients with a 100% electric commercial vehicles fleet, fair and sustainable working conditions for our employees and a unique professional customer-focused mindset
- We see ourselves as a professional services company who strongly cares about the environment, clients and their customers, and its employees

Attachements
- Company logos - see attached
- Licensed pictures (feel free to use in the designs ) - see here: https://www.filecrate-share.com/sh/72qplmwx39z114b/BBxkTqZr8nVoLpWeHdYUFa3Kcm?dl=0

Requirements
Must have
• We are thinking about at least the following content templates:

- intro/outro (e.g., title, agenda, transition, team, goals, about us, executive summary, key take aways, thank you)
- charts and graphs (e.g., pie, doughnut, bar, line, waterfall, venn)
- image and video (e.g., image only, large image with a sentence)
- text (e.g., text only, text with graph, text with 3/4/5 categories, key numbers)
- process (e.g., steps, phases)
- funnels
- pyramid
- frameworks (with 2/3/4/5 categories)
- timeline (e.g., general/project timeline, gantt)
- services offer
- KPIs/scorecard
- vision, mission, values, culture
- evaluation results
- activities/ToDo page
- policy
- career path
- icons page

Hope this helps. Pls see this as wish list as some of them can also be built by the content from the other slides

```html
<!DOCTYPE html>
<html lang="en">
<head>
<meta charset="utf-8">
<title>Brookvane Freight – Presentation Template Overview</title>
<link href="https://fonts.googleapis.com/css2?family=Poppins:wght@300;400;500;600;700&display=swap" rel="stylesheet">
<style>
:root{
  --green:#8cc63f;
  --green-dark:#2f9b46;
  --green-deep:#1f7a36;
  --ink:#222222;
  --slate:#3b3b3b;
  --grey:#6f6f6f;
  --light:#f2f2f2;
  --page:#dcdcdc;
  --band:#111111;
  --red:#d8322b;
}
*{box-sizing:border-box;margin:0;padding:0}
html,body{width:1200px;height:4199px;overflow:hidden}
body{position:relative;background:var(--page);font-family:"Poppins",sans-serif;color:var(--ink)}
.page-brand{position:absolute;left:36px;top:40px;display:flex;align-items:center;gap:8px;font-size:15px;font-weight:600;color:var(--green-dark)}
.page-brand .dot{width:22px;height:22px;border-radius:50%;background:var(--green)}

.slide{position:absolute;width:540px;height:304px;overflow:hidden;background:#fff}
.slide.hero{left:277px;top:90px;transform:scale(1.1963);transform-origin:0 0}
.photo{position:absolute}
.abs{position:absolute}

/* green accent shapes */
.arc{position:absolute;border-radius:50%;pointer-events:none}
.arc.deep{background:var(--green-deep);opacity:.55}
.arc.lime{background:var(--green);opacity:.6}
.arc.solid{background:linear-gradient(135deg,var(--green) 0%,var(--green-dark) 100%)}

.brand{position:absolute;display:flex;align-items:center;gap:4px;font-weight:600;white-space:nowrap;z-index:2}
.brand .dot{border-radius:50%;background:var(--green)}
.brand-title{left:44px;top:52px;font-size:11px;color:var(--green)}
.brand-title .dot{width:16px;height:16px}
.brand-foot{left:12px;bottom:9px;font-size:6.5px;color:var(--green-dark)}
.brand-foot .dot{width:9px;height:9px}
.brand-foot.on-dark{color:#fff}
.page-num{position:absolute;right:10px;bottom:10px;width:16px;height:8px;border-radius:4px;background:var(--green);color:#fff;font-size:4.5px;text-align:center;line-height:8px}

.t-title{position:absolute;left:44px;top:106px;font-size:30px;line-height:32px;font-weight:600;color:var(--green);letter-spacing:-.5px;z-index:2}
.t-sub{position:absolute;left:44px;top:182px;font-size:19px;font-weight:400;color:#fff;z-index:2}
.t-date{position:absolute;left:44px;top:229px;font-size:7px;color:#ddd;z-index:2}
.t-band{position:absolute;left:0;bottom:0;width:100%;height:18px;background:var(--band);color:#ccc;font-size:4.5px;text-align:center;line-height:18px;z-index:3}
.title-slide.light .t-sub{color:var(--ink)}
.title-slide.light .t-date{color:var(--grey)}

.kicker{position:absolute;font-size:6px;color:var(--green);text-transform:uppercase;letter-spacing:.3px}
.kicker.plain{text-transform:none}
.center{left:0;width:100%;text-align:center}
.h2{position:absolute;font-size:19px;font-weight:400;color:var(--ink)}
.h2 b{font-weight:600}
.divider-dot{position:absolute;width:6px;height:6px;border-radius:50%;background:var(--green);left:267px}
.lede{position:absolute;left:50px;width:440px;text-align:center;font-size:6.5px;line-height:8px;color:var(--slate)}
.body-s{font-size:6px;line-height:7.5px;color:var(--slate)}

.toc-item{position:absolute;display:flex;gap:10px;align-items:flex-start}
.toc-num{font-size:16px;font-weight:300;color:#b5b5b5;line-height:18px;width:12px}
.toc-text{font-size:11px;line-height:12px}
.toc-text span{display:block;color:var(--green-dark)}

.card{position:absolute;background:#fff;padding:10px 12px}
.card h3{font-size:17px;font-weight:400;text-align:center;margin-bottom:8px}
.card h3 span{color:var(--green)}
.card p{font-size:6.5px;line-height:8px;text-align:center;color:var(--slate)}
.mv-card{position:absolute;background:#fff;padding:8px 12px;width:289px}
.mv-card h4{font-size:13px;font-weight:400;display:flex;align-items:center;gap:5px;margin-bottom:5px}
.mv-card h4::before{content:"";width:6px;height:6px;border-radius:50%;background:var(--green)}
.mv-card h4 span{color:var(--green-dark)}
.mv-card p{font-size:6px;line-height:7.5px;color:var(--slate)}

.member{position:absolute;top:92px;width:90px;text-align:center}
.avatar{width:62px;height:62px;border-radius:50%;margin:0 auto 14px;background:linear-gradient(180deg,#bfb3a6 0%,#9a7f68 55%,#5c4a3d 100%);border:2px solid #eee}
.member .name{font-size:9px;color:var(--green-dark)}
.member .role{font-size:6px;font-weight:600;margin:3px 0 5px}

.tr-small{position:absolute;left:52px;top:205px;font-size:11px;color:#fff;z-index:2}
.tr-big{position:absolute;left:52px;top:220px;font-size:28px;font-weight:500;color:var(--green);line-height:34px;z-index:2}

.svc{position:absolute;text-align:center;width:104px}
.svc .thumb{width:104px;height:103px}
.svc .label{font-size:7px;line-height:8px;color:var(--green-dark);margin-top:5px}
.svc-round{position:absolute;text-align:center;width:110px}
.svc-round .thumb{width:76px;height:76px;border-radius:50%;margin:0 auto}
.svc-round .label{font-size:7px;line-height:8px;color:var(--green-dark);margin:5px 0 4px}

.feat-title{position:absolute;font-size:18px;line-height:19px;font-weight:500;color:var(--ink)}
.feat-row{position:absolute;left:386px;width:145px;display:flex;gap:9px;align-items:flex-start}
.ic{flex:none;width:24px;height:24px;border-radius:50%;background:var(--green);border:2px solid #fff;box-shadow:0 0 0 1px #d6e9c0;display:flex;align-items:center;justify-content:center}
.ic svg{width:12px;height:12px;fill:#fff}
.feat-row h5{font-size:8px;font-weight:400;color:var(--green-dark);margin-bottom:2px}
.col3{position:absolute;width:140px;text-align:center}
.col3 .ic{width:30px;height:30px;margin:0 auto 5px}
.col3 .ic svg{width:14px;height:14px}
.col3 h5{font-size:8px;font-weight:400;color:var(--green-dark);margin-bottom:2px}
.aside-text{position:absolute;left:232px;top:44px;width:140px;font-size:8px;line-height:9px;color:var(--slate)}

.compare{position:absolute;top:120px;width:150px;text-align:center}
.compare h5{font-size:9px;line-height:10px;font-weight:400;margin-bottom:8px}
.compare.old h5{color:var(--red);text-decoration:line-through}
.compare.new h5{color:var(--green-dark)}
.compare li{list-style:none;font-size:6px;line-height:10.5px;color:var(--slate)}
.compare.old li:last-child{text-decoration:line-through}

.data-table{position:absolute;left:183px;top:88px;width:335px;border-collapse:collapse;font-size:6.5px}
.data-table th{background:var(--green-deep);color:#fff;font-weight:500;text-align:left;padding:3px 6px;height:16px}
.data-table th.yr{text-align:center;color:var(--green)}
.data-table td{padding:2px 6px;height:17px;border-bottom:1px solid #e2e2e2;color:var(--slate)}
.data-table td.n{text-align:center}

.tl{position:absolute;width:74px;height:74px;border-radius:50%;border:5px solid var(--green);display:flex;align-items:center;justify-content:center;background:#fff}
.tl.alt{border-color:var(--green-dark)}
.tl .core{width:56px;height:56px;border-radius:50%;background:var(--green-dark);display:flex;align-items:center;justify-content:center}
.tl.alt .core{background:var(--green)}
.tl svg{width:26px;height:26px;fill:#fff}
.tl-year{position:absolute;width:80px;text-align:center;font-size:14px;color:var(--green-dark)}
.tl-year small{display:block;font-size:5.5px;line-height:6.5px;color:var(--slate)}
.tl-note{position:absolute;width:80px;text-align:center;font-size:5.5px;line-height:6.5px;color:var(--slate)}

.contact-line{position:absolute;left:44px;display:flex;align-items:center;gap:5px;font-size:7px;color:#fff;z-index:2}
.contact-line svg{width:8px;height:8px;fill:#fff}
</style>
</head>
<body>

<svg width="0" height="0" style="position:absolute" aria-hidden="true">
  <defs>
    <symbol id="i-bulb" viewBox="0 0 24 24"><path d="M12 2a7 7 0 0 0-4 12.7V18h8v-3.3A7 7 0 0 0 12 2zM9 20h6v2H9z"/></symbol>
    <symbol id="i-search" viewBox="0 0 24 24"><path d="M10 3a7 7 0 1 0 4.2 12.6l5.6 5.6 1.4-1.4-5.6-5.6A7 7 0 0 0 10 3zm0 2a5 5 0 1 1 0 10 5 5 0 0 1 0-10z"/></symbol>
    <symbol id="i-list" viewBox="0 0 24 24"><path d="M5 3h14v18H5zM8 7v2h8V7zm0 4v2h8v-2zm0 4v2h6v-2z"/></symbol>
    <symbol id="i-pin" viewBox="0 0 24 24"><path d="M12 2a7 7 0 0 0-7 7c0 5 7 13 7 13s7-8 7-13a7 7 0 0 0-7-7zm0 4a3 3 0 1 1 0 6 3 3 0 0 1 0-6z"/></symbol>
    <symbol id="i-clock" viewBox="0 0 24 24"><path d="M12 2a10 10 0 1 0 0 20 10 10 0 0 0 0-20zm0 2a8 8 0 1 1 0 16 8 8 0 0 1 0-16zm-1 3v6l5 3 1-1.6-4-2.4V7z"/></symbol>
    <symbol id="i-phone" viewBox="0 0 24 24"><path d="M6.6 10.8a15 15 0 0 0 6.6 6.6l2.2-2.2a1 1 0 0 1 1-.25 11 11 0 0 0 3.6.6 1 1 0 0 1 1 1V20a1 1 0 0 1-1 1A17 17 0 0 1 3 4a1 1 0 0 1 1-1h3.5a1 1 0 0 1 1 1c0 1.25.2 2.45.6 3.6a1 1 0 0 1-.25 1z"/></symbol>
    <symbol id="i-user" viewBox="0 0 24 24"><path d="M12 3a4 4 0 1 1 0 8 4 4 0 0 1 0-8zm0 10c4.4 0 8 2 8 4.5V21H4v-3.5C4 15 7.6 13 12 13z"/></symbol>
    <symbol id="i-grid" viewBox="0 0 24 24"><path d="M3 5h18v15H3zm2 4v3h4V9zm6 0v3h4V9zm6 0v3h2V9zM5 14v3h4v-3zm6 0v3h4v-3zm6 0v3h2v-3z"/></symbol>
    <symbol id="i-flag" viewBox="0 0 24 24"><path d="M5 2h2v20H5zm3 1h11l-3 4 3 4H8z"/></symbol>
    <symbol id="i-chart" viewBox="0 0 24 24"><path d="M3 20h18v2H3zm2-8h3v7H5zm5-4h3v11h-3zm5 3h3v8h-3z"/></symbol>
    <symbol id="i-star" viewBox="0 0 24 24"><path d="M12 2l3 6.5 7 .8-5.2 4.8 1.4 7L12 17.6 5.8 21l1.4-7L2 9.3l7-.8z"/></symbol>
    <symbol id="i-tick" viewBox="0 0 24 24"><path d="M9 16.2 4.8 12l-1.4 1.4L9 19 21 7l-1.4-1.4z"/></symbol>
    <symbol id="i-mail" viewBox="0 0 24 24"><path d="M2 4h20v16H2zm2 2v1l8 5 8-5V6z"/></symbol>
    <symbol id="i-globe" viewBox="0 0 24 24"><path d="M12 2a10 10 0 1 0 0 20 10 10 0 0 0 0-20zm6.9 9h-3a15 15 0 0 0-1.4-6A8 8 0 0 1 18.9 11zM12 4.1A13 13 0 0 1 13.9 11h-3.8A13 13 0 0 1 12 4.1zM9.5 5a15 15 0 0 0-1.4 6h-3A8 8 0 0 1 9.5 5zM5.1 13h3a15 15 0 0 0 1.4 6A8 8 0 0 1 5.1 13zm6.9 6.9A13 13 0 0 1 10.1 13h3.8A13 13 0 0 1 12 19.9zm2.5-.9a15 15 0 0 0 1.4-6h3a8 8 0 0 1-4.4 6z"/></symbol>
  </defs>
</svg>

<div class="page-brand"><span class="dot"></span>Brookvane Freight</div>

<!-- Hero title slide -->
<section class="slide hero title-slide">
  <div class="photo" style="inset:0;background:linear-gradient(100deg,#262626 0%,#3a3a3a 35%,#5b5b58 65%,#787570 100%)" role="img" aria-label="Man with glasses working on a laptop in an office"></div>
  <div class="arc deep" style="left:340px;top:-60px;width:320px;height:400px"></div>
  <div class="brand brand-title"><span class="dot"></span>Brookvane Freight</div>
  <h1 class="t-title">Presentation<br>Title Goes Here!</h1>
  <p class="t-sub">Subtitle of Presentation</p>
  <p class="t-date">Tuesday, April 27, 2021</p>
  <footer class="t-band">Copyright © 2020 Brookvane Freight · All Rights Reserved</footer>
</section>

<!-- Row 1 -->
<section class="slide title-slide" style="left:51px;top:600px">
  <div class="photo" style="inset:0;background:linear-gradient(100deg,#262626 0%,#3a3a3a 35%,#5b5b58 65%,#787570 100%)" role="img" aria-label="Man with glasses working on a laptop in an office"></div>
  <div class="arc deep" style="left:340px;top:-60px;width:320px;height:400px"></div>
  <div class="brand brand-title"><span class="dot"></span>Brookvane Freight</div>
  <h1 class="t-title">Presentation<br>Title Goes Here!</h1>
  <p class="t-sub">Subtitle of Presentation</p>
  <p class="t-date">Tuesday, April 27, 2021</p>
  <footer class="t-band">Copyright © 2020 Brookvane Freight · All Rights Reserved</footer>
</section>

<section class="slide title-slide" style="left:610px;top:600px">
  <div class="photo" style="inset:0;background:linear-gradient(100deg,#282624 0%,#4a3c32 40%,#6e5848 70%,#3c2f27 100%)" role="img" aria-label="Many hands together holding a small seedling"></div>
  <div class="arc deep" style="left:340px;top:-60px;width:320px;height:400px"></div>
  <div class="brand brand-title"><span class="dot"></span>Brookvane Freight</div>
  <h1 class="t-title">Presentation<br>Title Goes Here!</h1>
  <p class="t-sub">Subtitle of Presentation</p>
  <p class="t-date">Tuesday, April 27, 2021</p>
  <footer class="t-band">Copyright © 2020 Brookvane Freight · All Rights Reserved</footer>
</section>

<!-- Row 2 -->
<section class="slide title-slide light" style="left:51px;top:921px">
  <div class="photo" style="inset:0;background:linear-gradient(100deg,#f6f6f6 0%,#e6e6e6 40%,#cfcfcd 70%,#bdbab5 100%)" role="img" aria-label="Faded photo of man working on a laptop in an office"></div>
  <div class="arc lime" style="left:340px;top:-60px;width:320px;height:400px"></div>
  <div class="brand brand-title"><span class="dot"></span>Brookvane Freight</div>
  <h1 class="t-title">Presentation<br>Title Goes Here!</h1>
  <p class="t-sub">Subtitle of Presentation</p>
  <p class="t-date">Tuesday, April 27, 2021</p>
  <footer class="t-band">Copyright © 2020 Brookvane Freight · All Rights Reserved</footer>
</section>

<section class="slide title-slide light" style="left:610px;top:921px">
  <div class="photo" style="inset:0;background:linear-gradient(100deg,#f6f6f6 0%,#ebe5df 40%,#d8cabd 70%,#c7b5a5 100%)" role="img" aria-label="Faded photo of hands holding a seedling"></div>
  <div class="arc lime" style="left:340px;top:-60px;width:320px;height:400px"></div>
  <div class="brand brand-title"><span class="dot"></span>Brookvane Freight</div>
  <h1 class="t-title">Presentation<br>Title Goes Here!</h1>
  <p class="t-sub">Subtitle of Presentation</p>
  <p class="t-date">Tuesday, April 27, 2021</p>
  <footer class="t-band">Copyright © 2020 Brookvane Freight · All Rights Reserved</footer>
</section>

<!-- Row 3: Table of contents -->
<section class="slide" style="left:51px;top:1242px">
  <p class="kicker plain" style="left:28px;top:26px">Brookvane Freight</p>
  <h2 class="h2" style="left:28px;top:34px">Table of <b>Contents</b></h2>
  <div class="toc-item" style="left:30px;top:104px"><span class="toc-num">1</span><p class="toc-text"><span>Title</span>Goes Here!</p></div>
  <div class="toc-item" style="left:172px;top:104px"><span class="toc-num">2</span><p class="toc-text"><span>Title</span>Goes Here!</p></div>
  <div class="toc-item" style="left:30px;top:147px"><span class="toc-num">3</span><p class="toc-text"><span>Title</span>Goes Here!</p></div>
  <div class="toc-item" style="left:172px;top:147px"><span class="toc-num">4</span><p class="toc-text"><span>Title</span>Goes Here!</p></div>
  <div class="toc-item" style="left:30px;top:190px"><span class="toc-num">5</span><p class="toc-text"><span>Title</span>Goes Here!</p></div>
  <div class="toc-item" style="left:172px;top:190px"><span class="toc-num">6</span><p class="toc-text"><span>Title</span>Goes Here!</p></div>
  <div class="toc-item" style="left:30px;top:233px"><span class="toc-num">7</span><p class="toc-text"><span>Title</span>Goes Here!</p></div>
  <div class="toc-item" style="left:172px;top:233px"><span class="toc-num">8</span><p class="toc-text"><span>Title</span>Goes Here!</p></div>
  <div class="arc solid" style="left:310px;top:96px;width:300px;height:300px"></div>
</section>

<!-- Row 3: Who we are -->
<section class="slide" style="left:610px;top:1242px;background:var(--light)">
  <div class="photo" style="left:0;top:0;width:540px;height:176px;background:linear-gradient(180deg,#9dc0e0 0%,#c8dcea 42%,#8ab550 58%,#5c8b35 100%)" role="img" aria-label="Green electric delivery van on a country road, labelled CO2-neutral"></div>
  <div class="card" style="left:289px;top:46px;width:203px;height:208px">
    <h3>Who <span>We Are</span></h3>
    <span class="abs" style="left:98px;top:36px;width:6px;height:6px;border-radius:50%;background:var(--green)"></span>
    <p style="margin-top:12px">Brookvane Freight is a pioneer in urban green logistics and provides zero-emissions last mile delivery services for its logistics and retail clients. We take on urban parcel delivery for our clients with a 100% electric commercial vehicles fleet, fair and sustainable working conditions for our employees and a unique professional customer-focused mindset.</p>
  </div>
  <p class="kicker" style="left:50px;top:202px">Introduction</p>
  <h2 class="h2" style="left:50px;top:212px">About Us</h2>
  <div class="brand brand-foot"><span class="dot"></span>Brookvane Freight</div>
  <span class="page-num">6</span>
</section>

<!-- Row 4: Mission & values -->
<section class="slide" style="left:51px;top:1565px;background:var(--light)">
  <div class="photo" style="left:0;top:0;width:342px;height:304px;background:linear-gradient(135deg,#3a4a66 0%,#7a5a44 35%,#a57c5c 55%,#5a4234 80%,#2f2620 100%)" role="img" aria-label="Many hands from above holding soil with a young plant"></div>
  <div class="mv-card" style="left:210px;top:41px;height:98px">
    <h4>Our <span>Mission</span></h4>
    <p>To satisfy consumers' ever-rising desire to buy products online, the CO2 emissions from delivery traffic will increase by 32% in the top 100 cities globally until 2030. Our clients care about our planet the same way we do, which is why Brookvane Freight helps to make the planet a better place by running the most environmentally friendly urban last mile possible.</p>
  </div>
  <div class="mv-card" style="left:210px;top:155px;height:98px">
    <h4>Our <span>Values</span></h4>
    <p>We see ourselves as a professional services company who strongly cares about the environment, clients and their customers, and its employees. We believe that delivering parcels CO2-free and providing a unique customer experience with a great team spirit are the cornerstones for Brookvane Freight to operate in today's world in a sustainable yet profitable way.</p>
  </div>
  <div class="brand brand-foot on-dark"><span class="dot"></span>Brookvane Freight</div>
  <span class="page-num">7</span>
</section>

<!-- Row 4: Team -->
<section class="slide" style="left:610px;top:1565px">
  <p class="kicker plain center" style="top:27px">Brookvane Freight</p>
  <h2 class="h2 center" style="top:35px">Meet Our Team</h2>
  <span class="divider-dot" style="top:66px"></span>
  <div class="member" style="left:21px"><div class="avatar" role="img" aria-label="Team member portrait"></div><p class="name">Person Name</p><p class="role">Lorem ipsum dolor</p><p class="body-s">Lorem ipsum dolor sit amet, at laborum nibh duis mauris. Per ultrices lectus sed metus.</p></div>
  <div class="member" style="left:122px"><div class="avatar" role="img" aria-label="Team member portrait"></div><p class="name">Person Name</p><p class="role">Lorem ipsum dolor</p><p class="body-s">Lorem ipsum dolor sit amet, at laborum nibh duis mauris. Per ultrices lectus sed metus.</p></div>
  <div class="member" style="left:224px"><div class="avatar" role="img" aria-label="Team member portrait"></div><p class="name">Person Name</p><p class="role">Lorem ipsum dolor</p><p class="body-s">Lorem ipsum dolor sit amet, at laborum nibh duis mauris. Per ultrices lectus sed metus.</p></div>
  <div class="member" style="left:326px"><div class="avatar" role="img" aria-label="Team member portrait"></div><p class="name">Person Name</p><p class="role">Lorem ipsum dolor</p><p class="body-s">Lorem ipsum dolor sit amet, at laborum nibh duis mauris. Per ultrices lectus sed metus.</p></div>
  <div class="member" style="left:427px"><div class="avatar" role="img" aria-label="Team member portrait"></div><p class="name">Person Name</p><p class="role">Lorem ipsum dolor</p><p class="body-s">Lorem ipsum dolor sit amet, at laborum nibh duis mauris. Per ultrices lectus sed metus.</p></div>
  <div class="brand brand-foot"><span class="dot"></span>Brookvane Freight</div>
  <span class="page-num">8</span>
</section>

<!-- Row 5: Services transition -->
<section class="slide" style="left:51px;top:1886px;background:#353535">
  <div class="photo" style="left:250px;top:0;width:290px;height:304px;background:linear-gradient(100deg,#353535 0%,#5a5a5a 30%,#4a6fa0 55%,#2f8a4a 80%,#d9d9d9 100%)" role="img" aria-label="Smiling delivery driver in a cap leaning out of a van window"></div>
  <div class="arc deep" style="left:380px;top:100px;width:240px;height:260px"></div>
  <p class="tr-small">What We Offer</p>
  <p class="tr-big">Our Services</p>
</section>

<!-- Row 5: Services square -->
<section class="slide" style="left:610px;top:1886px">
  <p class="kicker center" style="top:27px">What We Offer</p>
  <h2 class="h2 center" style="top:35px">Our Services</h2>
  <span class="divider-dot" style="top:64px"></span>
  <p class="lede" style="top:82px">Brookvane Freight provides last mile delivery services in urban areas to clients in the logistics and retail space. Our permanent employees are all highly trained and commit to highest professional standards which we continuously review and further develop with them.</p>
  <div class="svc" style="left:41px;top:110px"><div class="thumb" style="background:linear-gradient(160deg,#a9c9e4 0%,#7fb344 50%,#4d4d4d 100%)" role="img" aria-label="Electric van on a road"></div><p class="label">Zero-Emission<br>Delivery</p></div>
  <div class="svc" style="left:158px;top:110px"><div class="thumb" style="background:linear-gradient(160deg,#cfd6df 0%,#5f7da0 50%,#2a3443 100%)" role="img" aria-label="Business handshake"></div><p class="label">Professional All<br>Around</p></div>
  <div class="svc" style="left:276px;top:110px"><div class="thumb" style="background:linear-gradient(180deg,#6a6f75 0%,#24365f 55%,#c59b6c 100%)" role="img" aria-label="Courier holding a parcel"></div><p class="label">Highly Trained<br>Drivers</p></div>
  <div class="svc" style="left:393px;top:110px"><div class="thumb" style="background:linear-gradient(90deg,#1e2d26 0%,#35523f 45%,#efe6dc 100%)" role="img" aria-label="Customer receiving a parcel at the door"></div><p class="label">Rare Customer<br>Focus</p></div>
  <div class="brand brand-foot"><span class="dot"></span>Brookvane Freight</div>
  <span class="page-num">10</span>
</section>

<!-- Row 6: Services round -->
<section class="slide" style="left:51px;top:2208px">
  <p class="kicker center" style="top:27px">What We Offer</p>
  <h2 class="h2 center" style="top:35px">Our Services</h2>
  <span class="divider-dot" style="top:64px"></span>
  <p class="lede" style="top:82px">Brookvane Freight provides last mile delivery services in urban areas to clients in the logistics and retail space. Our permanent employees are all highly trained and commit to highest professional standards which we continuously review and further develop with them.</p>
  <div class="svc-round" style="left:40px;top:119px"><div class="thumb" style="background:linear-gradient(160deg,#a9c9e4 0%,#7fb344 50%,#4d4d4d 100%)" role="img" aria-label="Electric van on a road"></div><p class="label">Zero-Emission<br>Delivery</p><p class="body-s">We operate a 100% electric commercial vehicle fleet</p></div>
  <div class="svc-round" style="left:155px;top:119px"><div class="thumb" style="background:linear-gradient(160deg,#cfd6df 0%,#5f7da0 50%,#2a3443 100%)" role="img" aria-label="Business handshake"></div><p class="label">Professional All<br>Around</p><p class="body-s">We honor our commitments and hold ourselves to the highest professional standards</p></div>
  <div class="svc-round" style="left:274px;top:119px"><div class="thumb" style="background:linear-gradient(180deg,#6a6f75 0%,#24365f 55%,#c59b6c 100%)" role="img" aria-label="Courier holding a parcel"></div><p class="label">Highly Trained<br>Drivers</p><p class="body-s">We only employ permanently, train far above average, and live a great team spirit</p></div>
  <div class="svc-round" style="left:392px;top:119px"><div class="thumb" style="background:linear-gradient(90deg,#1e2d26 0%,#35523f 45%,#efe6dc 100%)" role="img" aria-label="Customer receiving a parcel"></div><p class="label">Rare Customer<br>Focus</p><p class="body-s">We live a customer-oriented mindset, always measuring ourselves against their experience</p></div>
  <div class="brand brand-foot"><span class="dot"></span>Brookvane Freight</div>
  <span class="page-num">11</span>
</section>

<!-- Row 6: Zero-emission -->
<section class="slide" style="left:610px;top:2208px">
  <p class="kicker" style="left:0;width:197px;text-align:center;top:26px">Our Services</p>
  <h2 class="feat-title" style="left:0;width:197px;text-align:center;top:36px">Zero-<br>Emission<br>Delivery</h2>
  <span class="abs" style="left:95px;top:100px;width:6px;height:6px;border-radius:50%;background:var(--green)"></span>
  <p class="abs" style="left:25px;top:112px;width:147px;text-align:center;font-size:8px;line-height:9px;color:var(--slate)">We operate a 100% electric commercial vehicle fleet</p>
  <div class="photo" style="left:197px;top:0;width:201px;height:304px;background:linear-gradient(170deg,#a8c47a 0%,#7ab53a 30%,#5f8f2f 48%,#6c6c6c 70%,#3a3a3a 100%)" role="img" aria-label="Green electric van driving on a road, close-up"></div>
  <div class="feat-row" style="top:62px"><span class="ic"><svg><use href="#i-bulb"/></svg></span><div><h5>Heading 1</h5><p class="body-s">Lorem ipsum dolor sit amet, at laborum nibh duis mauris. Per ultrices lectus sed metus.</p></div></div>
  <div class="feat-row" style="top:132px"><span class="ic"><svg><use href="#i-search"/></svg></span><div><h5>Heading 2</h5><p class="body-s">Lorem ipsum dolor sit amet, at laborum nibh duis mauris. Per ultrices lectus sed metus.</p></div></div>
  <div class="feat-row" style="top:202px"><span class="ic"><svg><use href="#i-list"/></svg></span><div><h5>Heading 3</h5><p class="body-s">Lorem ipsum dolor sit amet, at laborum nibh duis mauris. Per ultrices lectus sed metus.</p></div></div>
  <div class="brand brand-foot"><span class="dot"></span>Brookvane Freight</div>
  <span class="page-num">12</span>
</section>

<!-- Row 7: Professional -->
<section class="slide" style="left:51px;top:2529px">
  <p class="kicker" style="left:28px;top:26px">Our Services</p>
  <h2 class="feat-title" style="left:28px;top:36px">Professional<br>All Around</h2>
  <p class="aside-text">We honor our commitments and hold ourselves to the highest professional standards</p>
  <div class="photo" style="left:0;top:112px;width:540px;height:92px;background:linear-gradient(90deg,#dfe3e8 0%,#9aa9ba 30%,#4f6583 55%,#8a97a6 75%,#e6e8eb 100%)" role="img" aria-label="Two business people shaking hands"></div>
  <div class="col3" style="left:46px;top:189px"><span class="ic"><svg><use href="#i-bulb"/></svg></span><h5>Heading 1</h5><p class="body-s">Lorem ipsum dolor sit amet, at laborum nibh duis mauris. Per ultrices lectus.</p></div>
  <div class="col3" style="left:199px;top:189px"><span class="ic"><svg><use href="#i-grid"/></svg></span><h5>Heading 2</h5><p class="body-s">Lorem ipsum dolor sit amet, at laborum nibh duis mauris. Per ultrices lectus.</p></div>
  <div class="col3" style="left:352px;top:189px"><span class="ic"><svg><use href="#i-user"/></svg></span><h5>Heading 3</h5><p class="body-s">Lorem ipsum dolor sit amet, at laborum nibh duis mauris. Per ultrices lectus.</p></div>
  <div class="brand brand-foot"><span class="dot"></span>Brookvane Freight</div>
  <span class="page-num">13</span>
</section>

<!-- Row 7: Drivers -->
<section class="slide" style="left:610px;top:2529px">
  <p class="kicker" style="left:0;width:197px;text-align:center;top:26px">Our Services</p>
  <h2 class="feat-title" style="left:0;width:197px;text-align:center;top:36px">Highly<br>Trained<br>Drivers</h2>
  <span class="abs" style="left:95px;top:100px;width:6px;height:6px;border-radius:50%;background:var(--green)"></span>
  <p class="abs" style="left:25px;top:112px;width:147px;text-align:center;font-size:8px;line-height:9px;color:var(--slate)">We only employ permanently, train far above average, and live a great team spirit</p>
  <div class="photo" style="left:197px;top:0;width:201px;height:304px;background:linear-gradient(180deg,#8a7560 0%,#6b5a4a 20%,#24365f 45%,#1e2d52 72%,#c59b6c 100%)" role="img" aria-label="Smiling courier in a navy shirt carrying a cardboard box"></div>
  <div class="feat-row" style="top:62px"><span class="ic"><svg><use href="#i-user"/></svg></span><div><h5>Heading 1</h5><p class="body-s">Lorem ipsum dolor sit amet, at laborum nibh duis mauris. Per ultrices lectus sed metus.</p></div></div>
  <div class="feat-row" style="top:132px"><span class="ic"><svg><use href="#i-clock"/></svg></span><div><h5>Heading 2</h5><p class="body-s">Lorem ipsum dolor sit amet, at laborum nibh duis mauris. Per ultrices lectus sed metus.</p></div></div>
  <div class="feat-row" style="top:202px"><span class="ic"><svg><use href="#i-phone"/></svg></span><div><h5>Heading 3</h5><p class="body-s">Lorem ipsum dolor sit amet, at laborum nibh duis mauris. Per ultrices lectus sed metus.</p></div></div>
  <div class="brand brand-foot"><span class="dot"></span>Brookvane Freight</div>
  <span class="page-num">14</span>
</section>

<!-- Row 8: Customer focus -->
<section class="slide" style="left:51px;top:2850px">
  <p class="kicker" style="left:28px;top:26px">Our Services</p>
  <h2 class="feat-title" style="left:28px;top:36px">Rare Customer<br>Focus</h2>
  <p class="aside-text">We honor our commitments and hold ourselves to the highest professional standards</p>
  <div class="photo" style="left:0;top:112px;width:540px;height:92px;background:linear-gradient(90deg,#243040 0%,#2d3a48 20%,#f2f2f2 26%,#1b2a22 32%,#2f4a38 60%,#eadfd3 100%)" role="img" aria-label="Smiling woman receiving a parcel at her front door"></div>
  <div class="col3" style="left:46px;top:189px"><span class="ic"><svg><use href="#i-flag"/></svg></span><h5>Heading 1</h5><p class="body-s">Lorem ipsum dolor sit amet, at laborum nibh duis mauris. Per ultrices lectus.</p></div>
  <div class="col3" style="left:199px;top:189px"><span class="ic"><svg><use href="#i-chart"/></svg></span><h5>Heading 2</h5><p class="body-s">Lorem ipsum dolor sit amet, at laborum nibh duis mauris. Per ultrices lectus.</p></div>
  <div class="col3" style="left:352px;top:189px"><span class="ic"><svg><use href="#i-bulb"/></svg></span><h5>Heading 3</h5><p class="body-s">Lorem ipsum dolor sit amet, at laborum nibh duis mauris. Per ultrices lectus.</p></div>
  <div class="brand brand-foot"><span class="dot"></span>Brookvane Freight</div>
  <span class="page-num">15</span>
</section>

<!-- Row 8: Approach transition -->
<section class="slide" style="left:610px;top:2850px;background:#3a3a3a">
  <div class="photo" style="left:180px;top:0;width:360px;height:304px;background:radial-gradient(ellipse at 62% 38%,#8cad62 0%,#5f7a45 28%,#4a4f44 55%,#3a3a3a 100%)" role="img" aria-label="Hands holding soil with a small tree growing from it"></div>
  <div class="arc deep" style="left:330px;top:70px;width:260px;height:300px"></div>
  <p class="tr-small">Our Approach</p>
  <p class="tr-big" style="font-size:24px">Brookvane Freight</p>
</section>

<!-- Row 9: Comparison -->
<section class="slide" style="left:51px;top:3171px">
  <p class="kicker center" style="top:27px">Our Approach</p>
  <h2 class="h2 center" style="top:35px">Brookvane Freight Is</h2>
  <span class="divider-dot" style="top:64px"></span>
  <div class="photo" style="left:186px;top:76px;width:204px;height:180px;background:linear-gradient(90deg,#ffffff 0%,#7a7a7a 25%,#3c3c3c 48%,#4f8f2c 52%,#7cbf3f 75%,#ffffff 100%)" role="img" aria-label="Tree half bare and half in full green leaf"></div>
  <div class="compare old" style="left:26px">
    <h5>An Ordinary<br>Parcel Delivery Firm</h5>
    <ul><li>Polluting our cities</li><li>Always in a rush</li><li>Short-term oriented</li><li>Focusing on profit only</li><li>Yet another parcel delivery firm</li></ul>
  </div>
  <div class="compare new" style="left:366px">
    <h5>A Pioneering<br>Green Last Mile Firm</h5>
    <ul><li>Delivering parcels emissions-free</li><li>Putting customer experience first</li><li>Operating the business sustainably</li><li>Environment, customers and employees</li><li>A professional services company</li></ul>
  </div>
  <div class="brand brand-foot"><span class="dot"></span>Brookvane Freight</div>
  <span class="page-num">17</span>
</section>

<!-- Row 9: Chart -->
<section class="slide" style="left:610px;top:3171px">
  <p class="kicker plain" style="left:28px;top:26px">Heading</p>
  <h2 class="feat-title" style="left:28px;top:36px">Slide Title<br>Goes Here!</h2>
  <div class="feat-row" style="left:22px;top:120px;width:160px"><span class="ic"><svg><use href="#i-bulb"/></svg></span><p class="body-s">Lorem ipsum dolor sit amet, at laborum nibh duis mauris. Per ultrices lectus sed metus.</p></div>
  <div class="feat-row" style="left:22px;top:163px;width:160px"><span class="ic"><svg><use href="#i-search"/></svg></span><p class="body-s">Lorem ipsum dolor sit amet, at laborum nibh duis mauris. Per ultrices lectus sed metus.</p></div>
  <div class="feat-row" style="left:22px;top:206px;width:160px"><span class="ic"><svg><use href="#i-pin"/></svg></span><p class="body-s">Lorem ipsum dolor sit amet, at laborum nibh duis mauris. Per ultrices lectus sed metus.</p></div>
  <svg class="abs" style="left:190px;top:24px" width="182" height="250" viewBox="0 0 182 250" role="img" aria-label="Grouped bar chart for 2018 to 2021">
    <g font-family="Poppins,sans-serif" font-size="6" fill="#6f6f6f" text-anchor="end">
      <text x="12" y="227">0</text><text x="12" y="191">1</text><text x="12" y="155">2</text><text x="12" y="120">3</text><text x="12" y="84">4</text><text x="12" y="48">5</text><text x="12" y="12">6</text>
    </g>
    <line x1="18" y1="225" x2="178" y2="225" stroke="#cfcfcf" stroke-width="1"/>
    <g>
      <rect x="26" y="70" width="7" height="155" fill="#1f7a36"/><rect x="35" y="157" width="7" height="68" fill="#8cc63f"/><rect x="44" y="160" width="7" height="65" fill="#555"/>
      <rect x="66" y="140" width="7" height="85" fill="#1f7a36"/><rect x="75" y="62" width="7" height="163" fill="#8cc63f"/><rect x="84" y="160" width="7" height="65" fill="#555"/>
      <rect x="106" y="100" width="7" height="125" fill="#1f7a36"/><rect x="115" y="157" width="7" height="68" fill="#8cc63f"/><rect x="124" y="68" width="7" height="157" fill="#555"/>
      <rect x="146" y="136" width="7" height="89" fill="#1f7a36"/><rect x="155" y="60" width="7" height="165" fill="#8cc63f"/><rect x="164" y="35" width="7" height="190" fill="#555"/>
    </g>
    <g font-family="Poppins,sans-serif" font-size="6" fill="#6f6f6f" text-anchor="middle">
      <text x="38" y="238">2018</text><text x="78" y="238">2019</text><text x="118" y="238">2020</text><text x="158" y="238">2021</text>
    </g>
  </svg>
  <div class="photo" style="left:381px;top:0;width:159px;height:304px;background:linear-gradient(160deg,#d3d6da 0%,#8b9198 35%,#4a4f55 70%,#2f3236 100%)" role="img" aria-label="Man with glasses looking at a laptop screen"></div>
  <div class="brand brand-foot"><span class="dot"></span>Brookvane Freight</div>
  <span class="page-num">18</span>
</section>

<!-- Row 10: Table -->
<section class="slide" style="left:51px;top:3492px">
  <div class="photo" style="left:0;top:0;width:158px;height:304px;background:linear-gradient(160deg,#2e5a26 0%,#5e9636 35%,#8cbf52 55%,#2f5a2a 100%)" role="img" aria-label="Hand reaching towards green leaves"></div>
  <p class="kicker plain" style="left:184px;top:22px">Heading</p>
  <h2 class="feat-title" style="left:184px;top:32px;font-size:17px">Slide Title Goes Here!</h2>
  <table class="data-table">
    <tr><th>Heading</th><th class="yr">2019</th><th class="yr">2020</th><th class="yr">2021</th></tr>
    <tr><td>Lorem ipsum dolor sit</td><td class="n">34%</td><td class="n">56%</td><td class="n">45%</td></tr>
    <tr><td>Lorem ipsum dolor sit</td><td class="n">89%</td><td class="n">78%</td><td class="n">89%</td></tr>
    <tr><td>Lorem ipsum dolor sit</td><td class="n">78%</td><td class="n">23%</td><td class="n">10%</td></tr>
    <tr><td>Lorem ipsum dolor sit</td><td class="n">22%</td><td class="n">67%</td><td class="n">45%</td></tr>
    <tr><td>Lorem ipsum dolor sit</td><td class="n">45%</td><td class="n">90%</td><td class="n">20%</td></tr>
    <tr><td>Lorem ipsum dolor sit</td><td class="n">73%</td><td class="n">23%</td><td class="n">34%</td></tr>
    <tr><td>Lorem ipsum dolor sit</td><td class="n">71%</td><td class="n">45%</td><td class="n">81%</td></tr>
    <tr><td>Lorem ipsum dolor sit</td><td class="n">56%</td><td class="n">62%</td><td class="n">67%</td></tr>
    <tr><td>Lorem ipsum dolor sit</td><td class="n">33%</td><td class="n">56%</td><td class="n">91%</td></tr>
  </table>
  <div class="brand brand-foot on-dark"><span class="dot"></span>Brookvane Freight</div>
  <span class="page-num">19</span>
</section>

<!-- Row 10: Timeline -->
<section class="slide" style="left:610px;top:3492px">
  <p class="kicker center" style="top:24px">Heading</p>
  <h2 class="h2 center" style="top:32px">Slide Title Goes Here</h2>
  <span class="divider-dot" style="top:62px"></span>
  <div class="tl" style="left:56px;top:104px"><span class="core"><svg><use href="#i-bulb"/></svg></span></div>
  <div class="tl-year" style="left:53px;top:184px">2017<small>Lorem ipsum dolor sit amet, at laboru</small></div>
  <div class="tl-note" style="left:102px;top:108px">Lorem ipsum dolor sit amet, at laboru</div>
  <div class="tl-year" style="left:102px;top:124px">2018</div>
  <div class="tl alt" style="left:142px;top:162px"><span class="core"><svg><use href="#i-clock"/></svg></span></div>
  <div class="tl" style="left:230px;top:104px"><span class="core"><svg><use href="#i-pin"/></svg></span></div>
  <div class="tl-year" style="left:227px;top:184px">2019<small>Lorem ipsum dolor sit amet, at laboru</small></div>
  <div class="tl-note" style="left:280px;top:108px">Lorem ipsum dolor sit amet, at laboru</div>
  <div class="tl-year" style="left:280px;top:124px">2020</div>
  <div class="tl alt" style="left:320px;top:162px"><span class="core"><svg><use href="#i-tick"/></svg></span></div>
  <div class="tl" style="left:410px;top:104px"><span class="core"><svg><use href="#i-star"/></svg></span></div>
  <div class="tl-year" style="left:407px;top:184px">2021<small>Lorem ipsum dolor sit amet, at laboru</small></div>
  <div class="brand brand-foot"><span class="dot"></span>Brookvane Freight</div>
  <span class="page-num">20</span>
</section>

<!-- Contact -->
<section class="slide" style="left:331px;top:3815px">
  <div class="photo" style="inset:0;background:radial-gradient(ellipse at 55% 30%,#a6c27a 0%,#5d8a3c 25%,#3c6230 50%,#24401f 75%,#172a15 100%)" role="img" aria-label="Forest canopy seen from below"></div>
  <div class="brand brand-title" style="top:118px"><span class="dot"></span>Brookvane Freight</div>
  <p class="abs" style="left:44px;top:174px;font-size:13px;color:var(--green)">Contact Us</p>
  <p class="contact-line" style="top:196px"><svg viewBox="0 0 24 24"><use href="#i-phone"/></svg>+49 (0) 30 5550 1234</p>
  <p class="contact-line" style="top:210px"><svg viewBox="0 0 24 24"><use href="#i-mail"/></svg>info@brookvane-freight.de</p>
  <p class="contact-line" style="top:224px"><svg viewBox="0 0 24 24"><use href="#i-globe"/></svg>https://www.brookvane-freight.de</p>
  <footer class="t-band">Copyright © 2020 Brookvane Freight · All Rights Reserved</footer>
</section>

</body>
</html>
```